TV - business card

Tidewell Vantage is an insurance brokerage firm, inovative, proactive, vigorous, which aims to become the leader of the insurance brokers in Anfrica. We should like to get some designs which should be avoided also in Gray / Metallic for the Administration and Orange / Blue for the Managers (ike in the picture sent). The Blue / Green logo is not the correct one, but the source of the file. Please adjust the color accordingly for the business cards. 1 / Orange / Blue 2 / Gray / Metallic We want something classic but which is transmitted strenght, inovation, modernity and most of all, rapidity. We want something start-up like, very punchy and catching eye remaining profesional at the same time. Name: Delton Ashgrove Function: Managing Director Address: N ° 73/74 Cmt. Bolembe - R / C 2B Esquerda - Bairro Quimbuta - Luanda Tel: (+244) 947 385 619 Email: delton.ashgrove@tidewell-v.com Website: www.tidewell-v. com We want classic in the front and creative, colorfull at the back. The cards will be printed in relief, with very high quality of paper.
Industry/Entity Type
Insurance Broker
Colors
Designer to choose colors to be used in the design.
Look and feel

```html
<!DOCTYPE html>
<html lang="en">
<head>
<meta charset="utf-8">
<title>Tidewell Vantage – Business Card</title>
<link rel="stylesheet" href="https://fonts.googleapis.com/css2?family=Exo+2:wght@700&family=Roboto:wght@400;700&display=swap">
<style>
  :root {
    --backdrop: #e4e4e6;
    --card: #1c1c1e;
    --edge: #f26a1f;
    --orange: #f26a1f;
    --blue: #2e9ad8;
    --text: #d4d4d4;
    --muted: #9a9a9a;
  }
  html, body {
    margin: 0;
    width: 1200px;
    height: 1200px;
    overflow: hidden;
    background: var(--backdrop);
  }
  .canvas {
    position: relative;
    width: 1200px;
    height: 1200px;
  }
  .card {
    position: absolute;
    left: 160px;
    width: 880px;
    height: 503px;
    background: var(--card);
    border-bottom: 6px solid var(--edge);
    border-right: 6px solid var(--edge);
    box-sizing: border-box;
    box-shadow: 0 10px 26px rgba(0,0,0,0.25);
  }
  .card--contact { top: 70px; }
  .card--brand { top: 627px; }

  .brand-mark {
    display: flex;
    align-items: center;
    gap: 16px;
  }
  .brand-mark__dot {
    border-radius: 50%;
    background: var(--orange);
  }
  .brand-mark__name {
    font-family: "Exo 2", sans-serif;
    font-weight: 700;
    color: var(--orange);
    text-transform: uppercase;
    letter-spacing: 1px;
    white-space: nowrap;
  }

  /* contact side */
  .contact-brand {
    position: absolute;
    left: 40px;
    top: 0;
    width: 360px;
    height: 100%;
    display: flex;
    align-items: center;
    justify-content: center;
  }
  .contact-brand .brand-mark { flex-direction: column; gap: 22px; }
  .contact-brand .brand-mark__dot { width: 90px; height: 90px; }
  .contact-brand .brand-mark__name { font-size: 34px; }
  .divider {
    position: absolute;
    left: 420px;
    top: 60px;
    width: 3px;
    height: 380px;
    background: var(--orange);
  }
  .contact {
    position: absolute;
    left: 452px;
    top: 72px;
    right: 30px;
    font-family: "Roboto", sans-serif;
    color: var(--text);
  }
  .contact__name {
    margin: 0;
    font-size: 30px;
    font-weight: 700;
  }
  .contact__first { color: var(--orange); }
  .contact__last { color: var(--blue); }
  .contact__role {
    margin: 4px 0 40px;
    font-size: 17px;
    color: var(--muted);
  }
  .contact__address {
    margin: 0 0 28px;
    font-size: 15px;
    line-height: 1.5;
  }
  .contact__list {
    list-style: none;
    margin: 0;
    padding: 0;
    font-size: 15px;
  }
  .contact__item {
    display: flex;
    align-items: center;
    gap: 12px;
    margin-bottom: 12px;
  }
  .contact__icon { width: 18px; height: 18px; flex: none; }
  .label { color: var(--muted); }

  /* brand side */
  .card--brand .brand-mark {
    position: absolute;
    inset: 0;
    justify-content: center;
    gap: 22px;
  }
  .card--brand .brand-mark__dot { width: 70px; height: 70px; }
  .card--brand .brand-mark__name { font-size: 60px; }
</style>
</head>
<body>
<main class="canvas">

  <section class="card card--contact" aria-label="Business card, contact side">
    <div class="contact-brand">
      <div class="brand-mark">
        <span class="brand-mark__dot"></span>
        <span class="brand-mark__name">Tidewell Vantage</span>
      </div>
    </div>
    <div class="divider"></div>
    <div class="contact">
      <h1 class="contact__name"><span class="contact__first">Delton</span> <span class="contact__last">Ashgrove</span></h1>
      <p class="contact__role">Managing Director</p>
      <p class="contact__address"><span class="label">Address:</span> N ° 73/74 Cmt. Bolembe - R / C 2B<br>Esquerda - Bairro Quimbuta - Luanda</p>
      <ul class="contact__list">
        <li class="contact__item">
          <svg class="contact__icon" viewBox="0 0 24 24"><path fill="#f26a1f" d="M6.6 10.8a15 15 0 0 0 6.6 6.6l2.2-2.2a1 1 0 0 1 1-.25 11.4 11.4 0 0 0 3.6.57 1 1 0 0 1 1 1V20a1 1 0 0 1-1 1A17 17 0 0 1 3 4a1 1 0 0 1 1-1h3.5a1 1 0 0 1 1 1c0 1.25.2 2.45.57 3.57a1 1 0 0 1-.25 1z"/></svg>
          <span><span class="label">Tel:</span> (+244) 947 385 619</span>
        </li>
        <li class="contact__item">
          <svg class="contact__icon" viewBox="0 0 24 24"><rect x="3" y="5" width="18" height="14" rx="1.5" fill="none" stroke="#f26a1f" stroke-width="2"/><path d="M3.5 6l8.5 7 8.5-7" fill="none" stroke="#f26a1f" stroke-width="2"/></svg>
          <span><span class="label">Email:</span> delton.ashgrove@tidewell-v.com</span>
        </li>
        <li class="contact__item">
          <svg class="contact__icon" viewBox="0 0 24 24"><g fill="none" stroke="#f26a1f" stroke-width="2"><circle cx="12" cy="12" r="9"/><ellipse cx="12" cy="12" rx="4" ry="9"/><path d="M3 12h18"/></g></svg>
          <span><span class="label">Website:</span> www.tidewell-v. com</span>
        </li>
      </ul>
    </div>
  </section>

  <section class="card card--brand" aria-label="Business card, brand side">
    <div class="brand-mark">
      <span class="brand-mark__dot"></span>
      <span class="brand-mark__name">Tidewell Vantage</span>
    </div>
  </section>

</main>
</body>
</html>
```